TRK MECHANICAL FRONT WINDOWS DESIGN

I have two windows 2320 length, 1870 depth.
I would like a logo on one window, like the logo on sign we had designed with possibly the gears behind like in sign.
Other window would like same colours as logo with details of business.
The background colour I would maybe like the same as sign but if you think something looks better then happy to see design.
Details on other window:
ALL MECHANICAL REPAIRS, SERVICING AND MAJOR OVERHAULS ON LIGHT, HEAVY VEHICLES, DRILL RIGS, COMPRESSORS AND BOOSTERS
CERTIFIED VEHICLE REPAIRER
0451937264
tandkmechanical52@mailvane.net
Maybe just details in some sort of design or have a picture of a 46 SERIES dune strider, Brenk truck or an engine

```html
<!DOCTYPE html>
<html lang="en">
<head>
<meta charset="utf-8">
<title>TRK Mechanical – Window Details Panel</title>
<link href="https://fonts.googleapis.com/css2?family=Russo+One&family=Exo+2:ital,wght@0,700;1,700&display=swap" rel="stylesheet">
<style>
  :root {
    --ink: #3a3b3d;
    --ink-dark: #2b2c2e;
    --highlight: #ffffff;
    --steel-light: #e4e4e2;
    --steel-mid: #b9b8b4;
    --steel-dark: #6f6d69;
    --steel-deep: #4a4845;
  }
  * { margin: 0; padding: 0; box-sizing: border-box; }
  html, body {
    width: 1200px; height: 853px; overflow: hidden;
    background: #d9d9d9;
  }
  .window-panel {
    position: relative;
    width: 1200px; height: 853px;
    overflow: hidden;
    background:
      repeating-linear-gradient(0deg, rgba(255,255,255,0.05) 0 1px, rgba(0,0,0,0.04) 1px 3px),
      linear-gradient(180deg, #8d8b87 0%, #bdbcb8 6%, #f2f2f0 11%, #9d9b97 16%, #c9c8c4 28%, #a9a7a3 38%, #7a7874 42%, #c2c0bb 50%, #e7e6e2 54%, #8c8a86 60%, #cfcecb 66%, #f0f0ee 71%, #a7a5a1 77%, #c7c6c2 82%, #d9d8d5 100%);
  }
  .steel-band {
    position: absolute; left: 0; width: 100%;
    box-shadow: 0 2px 4px rgba(0,0,0,0.35), inset 0 1px 0 rgba(255,255,255,0.6);
  }
  .steel-band--top {
    top: 70px; height: 46px;
    background: linear-gradient(90deg, #8f8e8a 0%, #f4f4f2 20%, #a9a8a4 45%, #f7f7f5 65%, #9a9995 85%, #d8d7d4 100%);
  }
  .steel-band--middle {
    top: 372px; height: 140px;
    background:
      repeating-linear-gradient(0deg, rgba(255,255,255,0.06) 0 1px, rgba(0,0,0,0.05) 1px 3px),
      linear-gradient(90deg, #5f5d59 0%, #b8b6b1 18%, #7c7a76 35%, #d6d4cf 55%, #8a8884 72%, #c3c1bc 88%, #6d6b67 100%);
  }
  .steel-band--phone {
    top: 540px; height: 96px;
    background: linear-gradient(90deg, #9b9a96 0%, #f1f1ef 15%, #c4c3bf 40%, #f5f5f3 60%, #b0afab 82%, #e6e5e2 100%);
  }
  .text-emboss {
    color: var(--ink);
    text-shadow: 2px 2px 0 var(--highlight), 3px 3px 2px rgba(0,0,0,0.25);
  }
  .services {
    position: absolute; top: 140px; left: 0; width: 100%;
    text-align: center;
    font-family: "Russo One", sans-serif;
    font-size: 40px; line-height: 50px;
    letter-spacing: 1px; text-transform: uppercase;
  }
  .certified {
    position: absolute; top: 385px; left: 220px;
    display: flex; align-items: center; gap: 24px;
  }
  .certified__badge { width: 150px; height: 150px; filter: drop-shadow(3px 3px 0 #fff); }
  .certified__title {
    font-family: "Russo One", sans-serif;
    font-size: 84px; line-height: 84px; letter-spacing: 2px;
  }
  .certified__subtitle {
    font-family: "Russo One", sans-serif;
    font-size: 38px; line-height: 44px; letter-spacing: 1px;
    padding-left: 6px;
  }
  .phone {
    position: absolute; top: 548px; left: 240px;
    display: flex; align-items: center; gap: 20px;
  }
  .phone__icon { width: 58px; height: 72px; filter: drop-shadow(2px 2px 0 #fff); }
  .phone__number {
    font-family: "Russo One", sans-serif;
    font-size: 76px; letter-spacing: 4px;
  }
  .wave { position: absolute; left: 0; top: 650px; width: 1200px; height: 203px; }
  .email {
    position: absolute; top: 742px; left: 40px;
    display: flex; align-items: center; gap: 22px;
  }
  .email__icon { width: 82px; height: 62px; filter: drop-shadow(2px 2px 0 #fff); }
  .email__address {
    font-family: "Exo 2", sans-serif; font-style: italic; font-weight: 700;
    font-size: 46px;
  }
</style>
</head>
<body>
<main class="window-panel">
  <div class="steel-band steel-band--top"></div>
  <div class="steel-band steel-band--middle"></div>
  <div class="steel-band steel-band--phone"></div>

  <p class="services text-emboss">
    All mechanical repairs,<br>
    servicing and major overhauls<br>
    on light, heavy vehicles, drill rigs,<br>
    compressors and boosters
  </p>

  <div class="certified">
    <svg class="certified__badge" viewBox="0 0 150 150" aria-hidden="true">
      <circle cx="75" cy="75" r="72" fill="var(--ink-dark)"/>
      <circle cx="75" cy="75" r="54" fill="none" stroke="#d8d7d3" stroke-width="5"/>
      <path d="M48 77 L67 96 L103 58" fill="none" stroke="#d8d7d3" stroke-width="11" stroke-linecap="round" stroke-linejoin="round"/>
    </svg>
    <div>
      <div class="certified__title text-emboss">CERTIFIED</div>
      <div class="certified__subtitle text-emboss">VEHICLE REPAIRER</div>
    </div>
  </div>

  <div class="phone">
    <svg class="phone__icon" viewBox="0 0 58 72" aria-hidden="true">
      <path d="M14 4 L24 4 L27 20 L19 25 C21 38 26 47 34 54 L41 48 L54 55 L52 66 C46 70 38 70 30 64 C14 52 6 36 6 18 C6 10 9 6 14 4 Z" fill="var(--ink-dark)"/>
    </svg>
    <span class="phone__number text-emboss">0451937264</span>
  </div>

  <svg class="wave" viewBox="0 0 1200 203" preserveAspectRatio="none" aria-hidden="true">
    <defs>
      <linearGradient id="waveSteel" x1="0" y1="0" x2="1" y2="0">
        <stop offset="0" stop-color="#c9c8c4"/>
        <stop offset="0.3" stop-color="#f3f3f1"/>
        <stop offset="0.6" stop-color="#b7b6b2"/>
        <stop offset="0.85" stop-color="#eeeeec"/>
        <stop offset="1" stop-color="#a9a8a4"/>
      </linearGradient>
    </defs>
    <path d="M0 66 C300 -10 700 -10 1200 70 L1200 203 L0 203 Z" fill="#5a5955"/>
    <path d="M0 78 C300 8 700 8 1200 84 L1200 203 L0 203 Z" fill="url(#waveSteel)"/>
    <path d="M0 78 C300 8 700 8 1200 84" fill="none" stroke="#2e2d2b" stroke-width="5"/>
  </svg>

  <div class="email">
    <svg class="email__icon" viewBox="0 0 82 62" aria-hidden="true">
      <rect x="2" y="2" width="78" height="58" rx="8" fill="var(--ink-dark)"/>
      <path d="M8 10 L41 36 L74 10" fill="none" stroke="#dcdbd8" stroke-width="5" stroke-linejoin="round"/>
    </svg>
    <span class="email__address text-emboss">tandkmechanical52@mailvane.net</span>
  </div>
</main>
</body>
</html>
```